Briefpapier klangrabatt17
Die Zusammenarbeit war vorbildlich. Sehr schnelle Reaktion auf unsere Wünsche und eine sehr gute Umsetzung des Projektes. Danke, wir werden wieder auf Sie zurückkommen für unseren nächsten Flyer.
Zielgruppe
Wir verkaufen Musiknoten, Lehr-DVDs für Instrumente aus Klassik, Rock, Pop, Jazz etc.
Da wir in letzter Zeit mehr Musiknoten aus der Klassik haben, wäre es sinnvoll, den Briefbogen seriös zu gestalten.
Aufgabenstellung
Wir bitten um Gestaltung eines Briefbogens mit den folgenden Informationen:
Anschrift: klangrabatt17
www.klangrabatt17.example
Wir haben folgende Homepage:
http://laden.tonfinder.example/38527/Home.html
Der Zusatz lyra digital sollte allerdings nicht im Brieflogo erscheinen.
Also Logo nur mit "klangrabatt17" und dem Zusatz: Ihr Spezialist für Musiknoten und Lehr-DVD's
Bitte die in der angefügten Datei verwandten Farben verwenden (gelb und rot)

```html
<!DOCTYPE html>
<html lang="de">
<head>
<meta charset="utf-8">
<title>Briefpapier klangrabatt17</title>
<link href="https://fonts.googleapis.com/css2?family=Lato:wght@400;700;900&display=swap" rel="stylesheet">
<style>
  :root {
    --bg: #ebebec;
    --paper: #ffffff;
    --red: #c0201f;
    --orange: #e8842a;
    --ink: #1e1e1e;
    --muted: #444;
    --sig: #3a4a7a;
  }
  * { box-sizing: border-box; margin: 0; padding: 0; }
  html, body { width: 1200px; height: 943px; overflow: hidden; background: var(--bg); }
  body { font-family: 'Lato', sans-serif; color: var(--ink); position: relative; }

  .letterhead {
    position: absolute; left: 282px; top: 21px;
    width: 636px; height: 900px;
    background: var(--paper);
    box-shadow: 0 2px 10px rgba(0,0,0,.12);
    overflow: hidden;
  }
  .edge-band {
    position: absolute; left: 0; top: 0; width: 18px; height: 100%;
    background: linear-gradient(to bottom, var(--red) 0%, var(--red) 55%, var(--orange) 100%);
  }
  .corner-band {
    position: absolute; right: 0; top: 58px; width: 10px; height: 46px;
    background: linear-gradient(to bottom, var(--red), var(--orange));
  }

  .brand {
    position: absolute; right: 60px; top: 60px;
    display: flex; align-items: center; gap: 8px;
  }
  .brand-mark { width: 12px; height: 12px; background: var(--red); }
  .brand-name { font-weight: 700; font-size: 24px; line-height: 1; color: var(--ink); }

  .contact { position: absolute; right: 40px; top: 122px; font-size: 8.5px; line-height: 1.45; text-align: right; }
  .contact li { list-style: none; display: flex; justify-content: flex-end; align-items: center; gap: 6px; }
  .contact .dot { width: 7px; height: 7px; border-radius: 50%; background: var(--red); display: inline-block; }
  .contact .plain { padding-right: 13px; }
  .contact .gap { margin-top: 10px; }

  .sender-line {
    position: absolute; left: 70px; top: 222px; font-size: 6px; color: var(--muted);
    border-bottom: 0.6px solid var(--muted); padding-bottom: 1px;
  }
  .sender-line b { font-weight: 900; }

  .letter { position: absolute; left: 70px; top: 296px; width: 480px; font-size: 9.6px; line-height: 1.42; }
  .salutation { font-weight: 900; font-size: 11px; margin-bottom: 6px; }
  .letter p { margin-bottom: 13px; }
  .closing { margin-top: 2px; }
  .signature { display: block; margin: 8px 0 6px 20px; }
  .signer { font-weight: 700; }

  .footer { position: absolute; left: 70px; right: 30px; bottom: 46px; display: flex; font-size: 8.2px; line-height: 1.4; }
  .footer-col { flex: 1; padding: 0 14px; }
  .footer-col + .footer-col { border-left: 0.8px solid var(--ink); }
  .footer-col:first-child { padding-left: 0; }
  .footer-col h3 { color: var(--red); font-size: 9px; font-weight: 900; }
  .footer-col b { font-weight: 900; }
</style>
</head>
<body>
  <main class="letterhead">
    <div class="edge-band"></div>
    <div class="corner-band"></div>

    <header class="brand">
      <span class="brand-mark"></span>
      <span class="brand-name">klangrabatt17</span>
    </header>

    <ul class="contact">
      <li>04321-5580 <span class="dot"></span></li>
      <li>04321-55819 <span class="dot"></span></li>
      <li>klangrabatt17.example <span class="dot"></span></li>
      <li>www.klangrabatt17.example <span class="dot"></span></li>
      <li class="plain gap">info@klangrabatt17.example</li>
      <li class="plain">www.klangrabatt17.example</li>
    </ul>

    <div class="sender-line"><b>klangrabatt17</b> · Inh. Marlene Vogt · Ahornweg 8 · 24680 Musterfeld</div>

    <section class="letter">
      <div class="salutation">Dear John,</div>
      <p>Lorem ipsum dolor sit amet, consectetur adipiscing elit. Praesent non est diam. Vivamus risus sem, gravida sit amet nibh ut, ornare lobortis ante. Aliquam sollicitudin, mauris tincidunt semper venenatis, orci est pretium augue, ut vestibulum felis velit bibendum urna. Integer sollicitudin aliquet ligula, non ultricies nisl efficitur nec. Class aptent taciti sociosqu ad litora torquent per conubia nostra, per inceptos himenaeos. Quisque accumsan convallis vulputate. Vestibulum porta massa in rutrum hendrerit. Class aptent taciti sociosqu ad litora torquent per conubia nostra, per inceptos himenaeos. Aliquam felis lorem, facilisis ac condimentum quis, consectetur volutpat lacus. Proin fermentum sem quis elit efficitur, eu tempus magna maximus.</p>
      <p>Aenean a mi tortor. Morbi pretium mi sed cursus vehicula. Lorem ipsum dolor sit amet, consectetur adipiscing elit. In finibus eros ac maximus finibus. Nunc pretium pellentesque tellus. Nullam accumsan nisl non diam commodo sagittis. Nunc et ante sit amet urna auctor convallis. Maecenas sed fringilla metus, sit amet vulputate felis. Morbi eget tempor nisi. Aliquam erat volutpat. Aenean laoreet interdum tempus.</p>
      <p>Maecenas dignissim placerat mauris, vitae sollicitudin ex. Integer bibendum maximus mauris, ac tempor urna viverra id. Integer tincidunt lobortis nisl at posuere. Sed faucibus vulputate finibus. Maecenas convallis, sem quis pellentesque cursus, urna quam aliquam augue, quis porttitor eros est nec lectus. Sed mattis at tellus ut blandit. Aenean nunc magna, viverra sed mauris vel, porta finibus lacus. Nullam bibendum turpis rutrum porta placerat.</p>
      <div class="closing">Mit freundlichen Grüßen</div>
      <svg class="signature" width="140" height="40" role="img" aria-label="Handschriftliche Unterschrift">
        <rect x="0" y="6" width="140" height="28" rx="14" fill="var(--sig)" opacity="0.18"/>
      </svg>
      <div class="signer">Paul Berger</div>
      <div>Geschäftsführer</div>
    </section>

    <footer class="footer">
      <div class="footer-col">
        <h3>Anschrift:</h3>
        klangrabatt17<br>Inh. Marlene Vogt<br>Ahornweg 8, 24680 Musterfeld
      </div>
      <div class="footer-col">
        <h3>Unternehmen:</h3>
        <b>Geschäftsführer:</b> Marlene Vogt<br>
        <b>Steuernummer:</b> 000-111-22233<br>
        <b>UST-ID-Nr.:</b> DE 000000000
      </div>
      <div class="footer-col">
        <h3>Bankverbindung:</h3>
        Musterbank Nordtal<br>
        <b>BIC:</b> MUSTDEX1XXX<br>
        <b>IBAN:</b> DE00 1234 5678 0000 0000 00
      </div>
    </footer>
  </main>
</body>
</html>
```